BRIM Outreach Partners Business Card Rebrand

Hello Designers! We are looking for help designing our new business card to go in conjunction with our company rebrand. Unfortunately, we have an event mid June that requires we get these printed ASAP (before our new website is launched.) We have a mostly complete Brand Book which I have uploaded to this request for your reference to company information, style, fonts. I've also enclosed our logo file in .eps & .jpg. Attached is a sample business card my boss liked but said was "too simple." I made it in Canva and do not profess to be a designer. NOT FOR DESIGN REFERENCE, ONLY FOR CONTEXT Here is what our old website looks like: https://brimoutreachpartners.com/.

```html
<!DOCTYPE html>
<html lang="en">
<head>
<meta charset="utf-8">
<title>BRIM Outreach Partners – Business Card</title>
<link rel="stylesheet" href="https://fonts.googleapis.com/css2?family=Poppins:wght@400;600;700&display=swap">
<style>
  :root {
    --stage: #d1d2d4;
    --card: #ffffff;
    --brand-blue: #4aaee2;
    --ink: #0d0d0d;
    --text-grey: #555a5e;
    --band: #000000;
  }
  * { box-sizing: border-box; margin: 0; padding: 0; }
  html, body { width: 1200px; height: 1000px; overflow: hidden; }
  body {
    background: var(--stage);
    font-family: "Poppins", sans-serif;
    position: relative;
  }
  .card {
    position: absolute;
    left: 293px;
    width: 614px;
    height: 351px;
    overflow: hidden;
  }
  .card-front { top: 139px; background: var(--card); box-shadow: 0 0 1px rgba(0,0,0,.15); }
  .card-back { top: 509px; background: var(--brand-blue); }

  .wordmark {
    position: absolute;
    display: flex;
    align-items: center;
  }
  .wordmark-dot {
    border-radius: 50%;
    flex: none;
  }
  .wordmark-name {
    font-weight: 700;
    color: var(--ink);
    line-height: 1.02;
    letter-spacing: -0.3px;
  }
  .card-front .wordmark { left: 54px; top: 142px; gap: 12px; }
  .card-front .wordmark-dot { width: 50px; height: 50px; background: var(--brand-blue); }
  .card-front .wordmark-name { font-size: 22px; width: 165px; }

  .contact { position: absolute; left: 281px; top: 108px; }
  .contact-name { font-size: 19px; font-weight: 600; color: var(--ink); line-height: 26px; }
  .contact-role { font-size: 16.5px; font-weight: 400; color: var(--brand-blue); line-height: 22px; }
  .contact-list { list-style: none; margin-top: 16px; }
  .contact-list li {
    font-size: 14.5px;
    color: var(--text-grey);
    line-height: 22px;
    display: flex;
    align-items: center;
    gap: 7px;
  }
  .contact-list svg { width: 14px; height: 14px; fill: var(--brand-blue); flex: none; }

  .web-band { position: absolute; left: 258px; bottom: 0; width: 356px; height: 25px; }
  .web-band svg { position: absolute; inset: 0; }
  .web-band-url {
    position: absolute;
    left: 44px;
    top: 2px;
    font-size: 11.5px;
    letter-spacing: 1.3px;
    color: #ffffff;
  }

  .back-texture { position: absolute; inset: 0; background: var(--brand-blue); }
  .card-back .wordmark { left: 198px; top: 130px; gap: 12px; }
  .card-back .wordmark-dot { width: 90px; height: 90px; background: #ffffff; }
  .card-back .wordmark-name { font-size: 30px; width: 230px; }
</style>
</head>
<body>
  <section class="card card-front" aria-label="Business card front">
    <div class="wordmark">
      <span class="wordmark-dot"></span>
      <span class="wordmark-name">BRIM Outreach Partners</span>
    </div>

    <div class="contact">
      <p class="contact-name">Daniel Hurst-Moreau</p>
      <p class="contact-role">Managing Partner</p>
      <ul class="contact-list">
        <li>Riverton, Ga based (Central Time)</li>
        <li>
          <svg viewBox="0 0 16 16" aria-hidden="true"><path d="M1 6c0-2 3-4 7-4s7 2 7 4v1h-3.5V5.5h-7V7H1z M4 8h8l2 6H2z M8 9.5a2 2 0 1 0 0 4a2 2 0 0 0 0-4z"/></svg>
          555-214-0937
        </li>
        <li>
          <svg viewBox="0 0 16 16" aria-hidden="true"><path d="M1 3.5h14v1L8 9 1 4.5z M1 6l7 4.5L15 6v7H1z"/></svg>
          Daniel@brimoutreachpartners.com
        </li>
      </ul>
    </div>

    <div class="web-band">
      <svg viewBox="0 0 356 25" width="356" height="25" aria-hidden="true">
        <path d="M0 25 L22 0 H356 V25 Z" fill="var(--band)"/>
        <circle cx="14" cy="13" r="10" fill="var(--brand-blue)" stroke="#ffffff" stroke-width="2"/>
      </svg>
      <span class="web-band-url">www.brimoutreachpartners.com</span>
    </div>
  </section>

  <section class="card card-back" aria-label="Business card back">
    <div class="back-texture" role="img" aria-label="Embossed repeating brand pattern in light blue"></div>
    <div class="wordmark">
      <span class="wordmark-dot"></span>
      <span class="wordmark-name">BRIM Outreach Partners</span>
    </div>
  </section>
</body>
</html>
```